Post it Note design

POST-IT NOTE DESIGN (CONTENT)
Size recommended: 4x6 for handwriting space.
Header (Bold):
Lighting Issue Detected on Your Property
Sub-header:
During our routine night inspection, we noted the following item(s):
Checkbox List:
⬜ Building Lights Out
⬜ Pole Lights Out
⬜ Sign Not Illuminated
⬜ Other ________________________
Action Line:
We can provide a quote or dispatch service right away.
Area for notes
Contact Block (Bold & Centered):
Brovane Fixture Inc.
Service@BrovaneFixture.com
www.BrovaneFixture.com
877-514-0862
Industry/Entity Type
Electrical lighting
Colors
Designer to choose colors to be used in the design.
Look and feel
Each slider illustrates characteristics of the customer's brand and the style your logo design should communicate.

```html
<!DOCTYPE html>
<html lang="en">
<head>
<meta charset="utf-8">
<title>Brovane Fixture Inc. – Lighting Issue Notice</title>
<link href="https://fonts.googleapis.com/css2?family=Oswald:wght@600;700&family=Poppins:wght@400;600;700&display=swap" rel="stylesheet">
<style>
  :root {
    --backdrop: #8c8c8c;
    --paper: #ffffff;
    --brand-red: #ef3a43;
    --brand-red-soft: #f7a2a7;
    --brand-blue: #283786;
    --ink-dark: #1b1b1b;
    --rule: #9a9a9a;
    --sky-top: #6f9bd3;
    --sky-bottom: #b9c7d3;
    --truck-top: #e9ecef;
    --truck-bottom: #c9cdd2;
  }
  * { box-sizing: border-box; margin: 0; padding: 0; }
  html, body { width: 839px; height: 1200px; overflow: hidden; background: var(--backdrop); }
  .notice {
    position: absolute; left: 78px; top: 88px; width: 683px; height: 1025px;
    background: var(--paper); overflow: hidden;
    font-family: "Poppins", sans-serif;
  }
  .top-band { position: absolute; left: 0; top: 0; width: 683px; height: 27px; }
  .brand-name {
    position: absolute; left: 48px; top: 66px; width: 230px;
    font-family: "Poppins", sans-serif; font-weight: 700; font-size: 30px; line-height: 34px;
    color: var(--brand-red); text-transform: uppercase;
  }
  .headline-panel {
    position: absolute; left: 0; top: 171px; width: 353px; height: 187px;
    background: var(--brand-blue);
  }
  .headline {
    position: absolute; left: 46px; top: 22px;
    font-family: "Oswald", sans-serif; font-weight: 700; font-size: 41px; line-height: 45px;
    color: var(--paper); text-transform: uppercase; letter-spacing: 0.2px;
  }
  .photo-technician {
    position: absolute; left: 358px; top: 83px; width: 325px; height: 275px;
    background: linear-gradient(160deg, var(--sky-top), var(--sky-bottom));
  }
  .intro {
    position: absolute; left: 49px; top: 384px;
    font-weight: 600; font-size: 27px; line-height: 36px; white-space: nowrap;
  }
  .intro .lead { color: var(--brand-blue); display: block; }
  .intro .accent { color: var(--brand-red); display: block; }
  .check-item {
    position: absolute; display: flex; align-items: center;
    font-weight: 600; font-size: 23px; color: var(--brand-blue); white-space: nowrap;
  }
  .check-box {
    width: 37px; height: 35px; margin-right: 13px; flex: none;
    border: 1.5px solid var(--ink-dark); background: var(--paper);
    box-shadow: 3px 3px 0 var(--ink-dark);
  }
  .item-building { left: 48px; top: 499px; }
  .item-sign { left: 344px; top: 499px; }
  .item-pole { left: 48px; top: 600px; }
  .item-other { left: 344px; top: 600px; }
  .item-other .label { margin-left: 3px; }
  .fill-line { display: inline-block; width: 162px; border-bottom: 1.5px solid var(--ink-dark); margin-left: 8px; height: 22px; }
  .divider { position: absolute; top: 568px; height: 0; border-top: 1.5px solid var(--rule); }
  .divider-left { left: 48px; width: 274px; }
  .divider-right { left: 346px; width: 285px; }
  .action-band {
    position: absolute; left: 303px; top: 772px; width: 380px; height: 121px;
    background: var(--brand-red);
  }
  .action-text {
    position: absolute; left: 71px; top: 18px;
    font-family: "Oswald", sans-serif; font-weight: 600; font-size: 27px; line-height: 29px;
    color: var(--paper); text-transform: uppercase;
  }
  .photo-truck {
    position: absolute; left: 0; top: 673px; width: 356px; height: 250px;
    background: linear-gradient(180deg, var(--truck-top), var(--truck-bottom));
    border-radius: 0 40px 20px 0;
  }
  .contact-list { position: absolute; left: 48px; top: 928px; list-style: none; }
  .contact-list li {
    display: flex; align-items: center; height: 27px;
    font-size: 18.5px; color: var(--ink-dark);
  }
  .contact-list svg { width: 17px; height: 17px; margin-right: 8px; flex: none; }
  .phone-block { position: absolute; left: 392px; top: 936px; width: 291px; height: 70px; }
  .phone-number {
    position: absolute; left: 70px; top: 12px;
    font-family: "Oswald", sans-serif; font-weight: 700; font-size: 29px; line-height: 44px;
    color: var(--paper); letter-spacing: 0.5px;
  }
  .phone-icon { position: absolute; left: 36px; top: 23px; width: 24px; height: 24px; }
  .bottom-band { position: absolute; left: 0; top: 1010px; width: 683px; height: 15px; background: var(--brand-red); }
</style>
</head>
<body>
<main class="notice">
  <svg class="top-band" viewBox="0 0 683 27" aria-hidden="true">
    <polygon points="175,0 195,0 222,27 202,27" fill="var(--brand-red-soft)" opacity="0.5"/>
    <polygon points="203,0 222,0 249,27 230,27" fill="var(--brand-red-soft)" opacity="0.7"/>
    <polygon points="231,0 250,0 277,27 258,27" fill="var(--brand-red-soft)"/>
    <polygon points="259,0 272,0 299,27 286,27" fill="var(--brand-red)" opacity="0.85"/>
    <polygon points="280,0 683,0 683,27 307,27" fill="var(--brand-red)"/>
  </svg>

  <div class="brand-name">Brovane Fixture Inc.</div>

  <section class="headline-panel">
    <h1 class="headline">Lighting Issue<br>Detected on<br>Your Property</h1>
  </section>

  <div class="photo-technician" role="img" aria-label="Photo of a technician in a hard hat servicing a pole-mounted floodlight against a blue sky"></div>

  <p class="intro">
    <span class="lead">During our routine night inspection,</span>
    <span class="accent">we noted the following item(s)</span>
  </p>

  <div class="check-item item-building"><span class="check-box"></span><span class="label">Building Lights Out</span></div>
  <div class="check-item item-sign"><span class="check-box"></span><span class="label">Sign Not Illuminated</span></div>
  <div class="divider divider-left"></div>
  <div class="divider divider-right"></div>
  <div class="check-item item-pole"><span class="check-box"></span><span class="label">Pole Lights Out</span></div>
  <div class="check-item item-other"><span class="check-box"></span><span class="label">Other</span><span class="fill-line"></span></div>

  <div class="photo-truck" role="img" aria-label="Photo of a white bucket truck with traffic cones"></div>

  <section class="action-band">
    <p class="action-text">We can provide a<br>quote or dispatch<br>service right away</p>
  </section>

  <ul class="contact-list">
    <li>
      <svg viewBox="0 0 20 20" aria-hidden="true"><circle cx="10" cy="10" r="10" fill="var(--brand-blue)"/><rect x="5" y="6.5" width="10" height="7" fill="none" stroke="#fff" stroke-width="1.4"/><polyline points="5,6.5 10,10.5 15,6.5" fill="none" stroke="#fff" stroke-width="1.4"/></svg>
      Service@BrovaneFixture.com
    </li>
    <li>
      <svg viewBox="0 0 20 20" aria-hidden="true"><circle cx="10" cy="10" r="10" fill="var(--brand-blue)"/><circle cx="10" cy="10" r="5.5" fill="none" stroke="#fff" stroke-width="1.3"/><ellipse cx="10" cy="10" rx="2.3" ry="5.5" fill="none" stroke="#fff" stroke-width="1.2"/><line x1="4.5" y1="10" x2="15.5" y2="10" stroke="#fff" stroke-width="1.2"/></svg>
      www.BrovaneFixture.com
    </li>
  </ul>

  <div class="phone-block">
    <svg width="291" height="70" viewBox="0 0 291 70" aria-hidden="true" style="position:absolute;left:0;top:0">
      <polygon points="33,0 291,0 291,70 0,70" fill="var(--brand-blue)"/>
    </svg>
    <svg class="phone-icon" viewBox="0 0 24 24" aria-hidden="true">
      <circle cx="12" cy="12" r="11" fill="none" stroke="#fff" stroke-width="2"/>
      <path d="M8.2 6.5l2 2.6-1.1 1.4c.8 1.7 2 2.9 3.6 3.7l1.4-1.1 2.6 2-1.2 1.8c-4.3-.6-7.8-4.1-8.4-8.4z" fill="#fff"/>
    </svg>
    <span class="phone-number">877-514-0862</span>
  </div>

  <div class="bottom-band"></div>
</main>
</body>
</html>
```